Elegant wordpress web page for wedding rental of hand sanitizers

We want to rent our hand sanitizing towers out for high-end weddings. We need a very elegant, sophisticated page that describes our offering. You can see an ugly first draft here: trelvo.com/weddings
Target Market(s)
Wedding planners, wedding parents
Number of Pages Required
1 page
Font styles to use
Serif
Script
Colors
Designer to choose colors to be used in the design.
Requirements
Nice to have
- Two wedding-related sites for inspiration: quietorchardweddings-dot-com and fernlaneservices-dot-com

```html
<!DOCTYPE html>
<html lang="en">
<head>
<meta charset="utf-8">
<title>Trelvo Products – Wedding Sanitizer Towers</title>
<link href="https://fonts.googleapis.com/css2?family=Great+Vibes&family=Jost:wght@400;500;600&display=swap" rel="stylesheet">
<style>
:root{
  --brand:#1b8fd2;
  --ink:#3d3d3d;
  --ink-soft:#555;
  --button:#393939;
  --mist:#efefef;
  --white:#ffffff;
  --drop:#9fcbe6;
}
*{box-sizing:border-box;margin:0;padding:0}
html,body{width:1200px;height:4882px;overflow:hidden;background:var(--white)}
body{position:relative;font-family:"Jost",Arial,sans-serif;color:var(--ink)}
.backdrop{position:absolute;left:0;top:0;width:1200px;height:4882px}
.abs{position:absolute}
.site-header{position:absolute;left:0;top:0;width:1200px;height:123px;background:var(--white)}
.wordmark{position:absolute;left:150px;top:30px;font-family:"Jost",sans-serif;font-weight:600;font-size:58px;color:var(--brand);line-height:1}
.main-nav a{position:absolute;top:55px;font-size:17px;color:var(--brand);text-decoration:none}
.main-nav .active{border-bottom:4px solid var(--brand);padding-bottom:6px}
.search{position:absolute;left:1028px;top:52px}
.hero-title{position:absolute;left:520px;top:300px;width:520px;font-family:"Great Vibes",cursive;font-size:86px;line-height:94px;color:var(--white);text-shadow:0 2px 10px rgba(0,0,0,.35)}
.script-heading{font-family:"Great Vibes",cursive;font-weight:400;font-size:52px;line-height:50px;color:var(--ink)}
.intro{font-size:20px;line-height:26px;color:var(--ink-soft);margin-top:40px}
.features{list-style:none;margin-top:20px}
.features li{position:relative;padding-left:38px;font-size:20px;line-height:27px;color:var(--ink);margin-bottom:26px}
.features li svg{position:absolute;left:6px;top:10px}
.cta{position:absolute;display:flex;align-items:center;justify-content:center;width:318px;height:48px;border-radius:24px;background:var(--button);color:var(--white);font-size:15px;font-weight:600;letter-spacing:.3px;text-decoration:none}
.footer-social{position:absolute;left:540px;top:4676px;display:flex;gap:16px}
.footer-social span{width:28px;height:28px;background:var(--brand);border-radius:3px}
.copyright{position:absolute;left:0;top:4744px;width:1200px;text-align:center;font-size:14px;color:var(--ink-soft);letter-spacing:.3px}
.footer-mark{position:absolute;left:0;top:4790px;width:1200px;text-align:center;font-weight:600;font-size:46px;color:#c4c4c4}
</style>
</head>
<body>
<svg class="backdrop" viewBox="0 0 1200 4882" aria-hidden="true">
  <defs>
    <linearGradient id="heroTone" x1="0" y1="0" x2="1" y2="1">
      <stop offset="0" stop-color="#5a4a36"/><stop offset=".5" stop-color="#a7a59a"/><stop offset="1" stop-color="#d8b8b2"/>
    </linearGradient>
  </defs>
  <path d="M0 123H1200V758C900 640 300 650 0 758Z" fill="url(#heroTone)"/>
  <path d="M0 758C300 650 900 640 1200 758V758Z" fill="var(--mist)"/>
  <path d="M0 1507C400 1630 800 1620 1200 1507V2293C800 2220 400 2220 0 2293Z" fill="var(--mist)"/>
  <path d="M0 3032C400 3110 800 3110 1200 3032V3771C800 3700 400 3700 0 3771Z" fill="var(--mist)"/>
  <path d="M0 4586C400 4480 800 4480 1200 4586V4882H0Z" fill="var(--mist)"/>
</svg>

<header class="site-header">
  <div class="wordmark">trelvo</div>
  <nav class="main-nav">
    <a style="left:449px" href="#">About</a>
    <a class="active" style="left:563px" href="#">Products</a>
    <a style="left:700px" href="#">Industry Solutions</a>
    <a style="left:906px" href="#">Contact</a>
  </nav>
  <svg class="search" width="24" height="24" viewBox="0 0 24 24"><circle cx="10" cy="10" r="7" fill="none" stroke="#1b8fd2" stroke-width="3"/><path d="M15 15l6 6" stroke="#1b8fd2" stroke-width="3"/></svg>
</header>

<div class="abs" role="img" aria-label="Wedding aisle with flowers and a photo-topped sanitizer tower" style="left:0;top:123px;width:1200px;height:520px"></div>
<h1 class="hero-title">Welcome to Trelvo Products</h1>

<!-- Section: unique sanitizer -->
<div class="abs" style="left:148px;top:828px;width:470px">
  <h2 class="script-heading">Welcome your guests with something truly unique – a customized hand sanitizer</h2>
  <p class="intro">Why have a generic, industrial hand sanitizer when you could have something truly unique and different?</p>
  <ul class="features">
    <li><svg width="16" height="22" viewBox="0 0 16 22"><path d="M8 0C8 0 0 10 0 14a8 8 0 0016 0C16 10 8 0 8 0Z" fill="var(--drop)"/></svg>Customize the photo above the spout and the spout decoration</li>
    <li><svg width="16" height="22" viewBox="0 0 16 22"><path d="M8 0C8 0 0 10 0 14a8 8 0 0016 0C16 10 8 0 8 0Z" fill="var(--drop)"/></svg>Choose any size and shape photo you wish</li>
    <li><svg width="16" height="22" viewBox="0 0 16 22"><path d="M8 0C8 0 0 10 0 14a8 8 0 0016 0C16 10 8 0 8 0Z" fill="var(--drop)"/></svg>Choose from our standard spout decorations or design one of your own. We'll take care of producing and fitting it.</li>
  </ul>
</div>
<a class="cta" style="left:150px;top:1393px" href="#">CHECK PRICE AND AVAILABILITY</a>
<div class="abs" role="img" aria-label="Photo sanitizer tower at a wedding reception" style="left:626px;top:891px;width:480px;height:480px;border-radius:50%;background:radial-gradient(circle at 50% 40%,#e8ded6,#8a6a52);box-shadow:6px 8px 0 #e6e6e6"></div>

<!-- Section: any photo -->
<div class="abs" role="img" aria-label="Sanitizer tower with couple photo and cake spout among garden flowers" style="left:0;top:1592px;width:572px;height:621px;background:linear-gradient(135deg,#6f7f5a,#d9d4cc 60%,#f2ecea)"></div>
<div class="abs" style="left:629px;top:1660px;width:460px">
  <h2 class="script-heading">Customize your sanitizer with any photo, any size, any shape.</h2>
  <ul class="features" style="margin-top:34px">
    <li><svg width="16" height="22" viewBox="0 0 16 22"><path d="M8 0C8 0 0 10 0 14a8 8 0 0016 0C16 10 8 0 8 0Z" fill="var(--drop)"/></svg>Choose a photo of the happy couple, the proud parents, or anything else you wish</li>
    <li><svg width="16" height="22" viewBox="0 0 16 22"><path d="M8 0C8 0 0 10 0 14a8 8 0 0016 0C16 10 8 0 8 0Z" fill="var(--drop)"/></svg>Choose any size or shape you wish, up to 24x36"</li>
    <li><svg width="16" height="22" viewBox="0 0 16 22"><path d="M8 0C8 0 0 10 0 14a8 8 0 0016 0C16 10 8 0 8 0Z" fill="var(--drop)"/></svg>We take care of all production and customization</li>
  </ul>
</div>
<a class="cta" style="left:629px;top:2098px" href="#">CHECK PRICE AND AVAILABILITY</a>

<!-- Section: spouts -->
<div class="abs" style="left:152px;top:2390px;width:420px">
  <h2 class="script-heading">Choose one of our standard spouts, or design your own</h2>
  <ul class="features" style="margin-top:34px">
    <li><svg width="16" height="22" viewBox="0 0 16 22"><path d="M8 0C8 0 0 10 0 14a8 8 0 0016 0C16 10 8 0 8 0Z" fill="var(--drop)"/></svg>Choose one of our standard spouts - wedding cake, flower vase, or "just married" car.  More spout decorations will be added each month</li>
    <li><svg width="16" height="22" viewBox="0 0 16 22"><path d="M8 0C8 0 0 10 0 14a8 8 0 0016 0C16 10 8 0 8 0Z" fill="var(--drop)"/></svg>For an additional fee, our team of 3D designers will design, 3D print, and decorate a spout just for your event</li>
  </ul>
</div>
<a class="cta" style="left:150px;top:2894px" href="#">CHECK PRICE AND AVAILABILITY</a>
<div class="abs" role="img" aria-label="White reception hall with flower urns and a sanitizer tower" style="left:618px;top:2331px;width:411px;height:659px;border-radius:205px;background:linear-gradient(180deg,#e9d7da,#f3eef0 55%,#c9b9a3);box-shadow:8px 6px 0 #e6e6e6"></div>

<!-- Section: act of care -->
<svg class="abs" style="left:110px;top:3131px" width="443" height="564" viewBox="0 0 443 564" role="img" aria-label="Freestanding touchless sanitizer dispenser in a bright hallway">
  <defs><linearGradient id="dropTone" x1="0" y1="0" x2="0" y2="1"><stop offset="0" stop-color="#e4e7e6"/><stop offset=".6" stop-color="#bcb5ab"/><stop offset="1" stop-color="#8a6a4e"/></linearGradient></defs>
  <path d="M221 0C221 0 0 250 0 343a221 221 0 00443 0C443 250 221 0 221 0Z" fill="url(#dropTone)"/>
</svg>
<div class="abs" style="left:629px;top:3185px;width:450px">
  <h2 class="script-heading">Greet your guests with an act of care</h2>
  <ul class="features" style="margin-top:28px">
    <li><svg width="16" height="22" viewBox="0 0 16 22"><path d="M8 0C8 0 0 10 0 14a8 8 0 0016 0C16 10 8 0 8 0Z" fill="var(--drop)"/></svg>Make your friends and family feel welcome and safe with a rugged, durable hand sanitizer from Trelvo</li>
    <li><svg width="16" height="22" viewBox="0 0 16 22"><path d="M8 0C8 0 0 10 0 14a8 8 0 0016 0C16 10 8 0 8 0Z" fill="var(--drop)"/></svg>Our battery-powered dispensers are reliable, wireless, and touchless</li>
    <li><svg width="16" height="22" viewBox="0 0 16 22"><path d="M8 0C8 0 0 10 0 14a8 8 0 0016 0C16 10 8 0 8 0Z" fill="var(--drop)"/></svg>Filled with your choice from our wide range of sanitizing products</li>
  </ul>
</div>
<a class="cta" style="left:637px;top:3587px" href="#">CHECK PRICE AND AVAILABILITY</a>

<!-- Section: service -->
<div class="abs" style="left:148px;top:3925px;width:460px">
  <h2 class="script-heading">Sanitizing as a service means low upfront investment</h2>
  <ul class="features" style="margin-top:40px">
    <li><svg width="16" height="22" viewBox="0 0 16 22"><path d="M8 0C8 0 0 10 0 14a8 8 0 0016 0C16 10 8 0 8 0Z" fill="var(--drop)"/></svg>Purchase our tower outright, or lease it for a low monthly rate on a two-year plan</li>
    <li><svg width="16" height="22" viewBox="0 0 16 22"><path d="M8 0C8 0 0 10 0 14a8 8 0 0016 0C16 10 8 0 8 0Z" fill="var(--drop)"/></svg>Monthly lease plan includes sanitizing fluid, online reporting, one year warranty, and tower rental</li>
    <li><svg width="16" height="22" viewBox="0 0 16 22"><path d="M8 0C8 0 0 10 0 14a8 8 0 0016 0C16 10 8 0 8 0Z" fill="var(--drop)"/></svg>Prices start at $3 per day - less than a cup of coffee!  Volume discounts available</li>
  </ul>
</div>
<a class="cta" style="left:150px;top:4376px" href="#">CHECK PRICE AND AVAILABILITY</a>
<div class="abs" role="img" aria-label="Sanitizer tower with couple photo panel and cake-shaped spout" style="left:606px;top:3828px;width:374px;height:739px;background:linear-gradient(180deg,#d9d3cc,#f4ecec 60%,#cfcfcf)"></div>

<!-- Footer -->
<div class="footer-social" aria-label="Social links"><span></span><span></span><span></span></div>
<p class="copyright">© COPYRIGHT 2021 TRELVO, LLC · SITEMAP · PRIVACY POLICY</p>
<div class="footer-mark">trelvo</div>
</body>
</html>
```